Business Cards for new orthopaedic surgery practice

My husband and I are starting our own orthopaedic surgery practice. We are looking for a business card that is uniform, but one will have my name/title and the other will have his. You can just create one design with my name on it for now. But when I choose your design as the winning design I will ask that you add another copy with his name/title.

We are looking for classy, simple, elite all in one. We like dark blues/a little gold/yellow. Something that goes with our logo. We want our logo incorporated. Here is all the info you need:
Business name: RV Spine & Vitality Center
Location: 38915 North Bramble Ave
Palm Hollow, FL 33482
Phone: 954-218-4630
Fax: 954-571-2846
Email: info@myrvspine.example

Names: Lucinda Ferrow, M.D.
Board Certified Hand and Upper Extremity Surgeon

Emeka Dlunga, M.D.
Board Certified Hip & Knee Replacement/General Orthopaedic Surgeon

Can decide what you want to put on the back. Maybe a slogan:
Grounded in Care. Centered on You

I am just going to upload our logo. The only thing is if we select you as the winning design, the location, and phone numbers may change. We will need your help to update that once fully solidified.

Industry/Entity Type

Medical

Contact Information for Business Card

Colors
0054AA
0677BA
7BADD7
CADEEF
E8F1F8
0094D4
00A9DD
6FCCEA
C7EBF8
E9F6FB

Requirements
Must have
• class, appeal,
Should not have
• We want to air on the side of masculine if we are looking at masculine vs. feminine feel. But we still want it classy, sophisticated, and something we will love

```html
<!DOCTYPE html>
<html lang="en">
<head>
<meta charset="utf-8">
<title>RV Spine &amp; Vitality Center — Business Card</title>
<link href="https://fonts.googleapis.com/css2?family=Cinzel:wght@600;700&family=Montserrat:wght@400&family=Tinos&display=swap" rel="stylesheet">
<style>
  :root {
    --backdrop: #343944;
    --gold: #bf9752;
    --gold-text: #c9a15c;
    --navy-ink: #234187;
    --navy-panel: #173d7e;
  }
  * { margin: 0; padding: 0; box-sizing: border-box; }
  html, body { width: 1200px; height: 1200px; overflow: hidden; }
  body { background: var(--backdrop); position: relative; }

  .card {
    position: absolute;
    left: 184px;
    width: 828px;
    height: 455px;
    background: var(--gold);
    box-shadow: 3px 3px 4px rgba(0,0,0,0.45);
    overflow: hidden;
  }
  .card--front { top: 125px; }
  .card--back { top: 652px; }

  /* Front */
  .front-brand {
    position: absolute;
    left: 0; right: 0; top: 150px;
    text-align: center;
    color: var(--navy-ink);
    font-family: "Cinzel", serif;
    font-weight: 700;
  }
  .front-brand__dot {
    width: 26px; height: 26px; border-radius: 50%;
    background: var(--navy-ink);
    margin: 0 auto 26px;
  }
  .front-brand__main { font-size: 46px; line-height: 1; letter-spacing: 0.5px; }
  .front-brand__sub {
    display: flex; align-items: center; justify-content: center;
    gap: 16px; margin-top: 14px;
    font-size: 38px; line-height: 1; letter-spacing: 3px;
  }
  .front-brand__rule { display: block; width: 118px; height: 4px; }

  /* Back – left */
  .back-brand {
    position: absolute;
    left: 0; top: 0; width: 368px; height: 100%;
    display: flex; flex-direction: column; justify-content: center; align-items: center;
    color: var(--navy-ink);
    font-family: "Cinzel", serif;
    font-weight: 700;
    text-align: center;
  }
  .back-brand__name { font-size: 26px; line-height: 1.15; }
  .back-brand__slogan {
    margin-top: 16px;
    font-size: 16px;
    letter-spacing: 0.2px;
    font-variant: small-caps;
  }

  /* Back – right */
  .contact-panel {
    position: absolute;
    left: 368px; top: 0; width: 460px; height: 100%;
    background: var(--navy-panel);
    color: var(--gold-text);
  }
  .person__name {
    position: absolute; left: 35px; top: 82px;
    font-family: "Cinzel", serif; font-weight: 600;
    font-size: 31px; line-height: 1; white-space: nowrap;
  }
  .person__title {
    position: absolute; left: 36px; top: 125px;
    font-family: "Montserrat", sans-serif; font-size: 13px; white-space: nowrap;
  }
  .contact-row {
    position: absolute; left: 40px;
    display: flex; align-items: flex-start; gap: 14px;
    font-family: "Tinos", serif; font-size: 23px; line-height: 30px;
  }
  .contact-row svg { width: 24px; height: 24px; margin-top: 3px; fill: var(--gold-text); flex: none; }
  .contact-row--address { top: 196px; }
  .contact-row--phone { top: 278px; }
  .contact-row--fax { top: 318px; }
  .contact-row--email { top: 362px; }
</style>
</head>
<body>

<section class="card card--front">
  <div class="front-brand">
    <div class="front-brand__dot"></div>
    <div class="front-brand__main">RV SPINE &amp; VITALITY</div>
    <div class="front-brand__sub">
      <svg class="front-brand__rule" viewBox="0 0 118 4" preserveAspectRatio="none"><polygon points="0,2 118,0 118,4" fill="#234187"/></svg>
      <span>CENTER</span>
      <svg class="front-brand__rule" viewBox="0 0 118 4" preserveAspectRatio="none"><polygon points="0,0 118,2 0,4" fill="#234187"/></svg>
    </div>
  </div>
</section>

<section class="card card--back">
  <div class="back-brand">
    <div class="back-brand__name">RV Spine &amp;<br>Vitality Center</div>
    <div class="back-brand__slogan">Grounded in Care. Centered on You</div>
  </div>

  <div class="contact-panel">
    <div class="person__name">Lucinda Ferrow, M.D</div>
    <div class="person__title">Board Certified Hand and Upper Extremity Surgeon</div>

    <div class="contact-row contact-row--address">
      <svg viewBox="0 0 24 24"><path d="M12 1a8 8 0 0 0-8 8c0 6 8 14 8 14s8-8 8-14a8 8 0 0 0-8-8zm0 11a3 3 0 1 1 0-6 3 3 0 0 1 0 6z"/></svg>
      <div>38915 North Bramble Ave<br>Palm Hollow, FL 33482</div>
    </div>
    <div class="contact-row contact-row--phone">
      <svg viewBox="0 0 24 24"><path d="M6.6 10.8a15 15 0 0 0 6.6 6.6l2.2-2.2a1 1 0 0 1 1-.25 11.4 11.4 0 0 0 3.6.6 1 1 0 0 1 1 1V20a1 1 0 0 1-1 1A17 17 0 0 1 3 4a1 1 0 0 1 1-1h3.5a1 1 0 0 1 1 1c0 1.25.2 2.450.6 3.6a1 1 0 0 1-.25 1z"/></svg>
      <div>954-218-4630</div>
    </div>
    <div class="contact-row contact-row--fax">
      <svg viewBox="0 0 24 24"><path d="M2 8c2-4 18-4 20 0v2h-5V8H7v2H2zM6 11h12l3 9H3zm6 2.5a2.5 2.5 0 1 0 0 5 2.5 2.5 0 0 0 0-5z"/></svg>
      <div>954-571-2846</div>
    </div>
    <div class="contact-row contact-row--email">
      <svg viewBox="0 0 24 24"><path d="M2 5h20v14H2zm2 2v.4l8 6 8-6V7zm0 2.9V17h16V9.9l-8 6z"/></svg>
      <div>info@myrvspine.example</div>
    </div>
  </div>
</section>

</body>
</html>
```